Professional business card for the wholesale of metals, chemicals and waste

We are an established company in the wholesale trade of metals, chemicals and waste and are looking for a creative, professional design for our business card. The business card should reflect the values of our company - competence, reliability and innovative strength. It should convey both industry expertise and a modern, trustworthy image.
Important information for the design:

Logo: Our company logo must be prominently placed on the business card.
Colors: Please refer to the colors used on our website www.okr-gmbh.at. These colors should appear in the design to maintain the visual identity of our company.

QR Code: The business card should contain a QR code that contains all the information listed on the business card.
Font: Choose clear, easy-to-read fonts that reflect a modern, professional look.
Layout: The design should be clear and structured so that both text and visual elements (logo, QR code) are in a balanced relationship to each other.

Information that should appear on the business card:

Company name: OKR Handelsagenturen GmbH
Title: Dipl.-Ing.
Name: Lukas Fenwald
Position: Managing Director of Operations & Corporate Development
Phone: +43 4186 5921 48
Mobile: +43 664 58 37 216
Email: lukas.fenwald@okr-gmbh.at
Homepage: www.okr-gmbh.at

Design style:

Industry: Industrial yet modern style that conveys competence and trust.
Message: The business card should present our company as a leading supplier in the wholesale trade of metals, chemicals and waste – reliable, professional and innovative.
Target group: Our target group consists of B2B customers and industry contacts who are looking for high-quality products and services in the areas of metal trading, chemicals and waste management.

We look forward to creative designs that reflect our professional identity and are also modern and appealing. Your design should make a statement for our company!

```html
<!DOCTYPE html>
<html lang="en">
<head>
<meta charset="utf-8">
<title>OKR Handelsagenturen GmbH – Business Card</title>
<link href="https://fonts.googleapis.com/css2?family=Lato:wght@400;700;900&display=swap" rel="stylesheet">
<style>
  :root {
    --stage: #2a2b2e;
    --navy: #1e2556;
    --navy-deep: #1a2050;
    --navy-emboss: #232a5e;
    --navy-shade: #161b45;
    --white: #ffffff;
    --soft: rgba(255,255,255,0.82);
  }
  * { margin: 0; padding: 0; box-sizing: border-box; }
  html, body {
    width: 1200px; height: 952px; overflow: hidden;
    background: var(--stage);
    font-family: "Lato", sans-serif;
  }
  .sheet {
    width: 1200px; height: 952px;
    display: flex; flex-direction: column;
    align-items: center; justify-content: center; gap: 44px;
  }
  .card {
    width: 620px; height: 380px;
    background: linear-gradient(160deg, var(--navy) 0%, var(--navy-deep) 100%);
    border-radius: 4px;
    position: relative; overflow: hidden;
    box-shadow: 0 10px 30px rgba(0,0,0,0.45);
  }
  /* front */
  .card-front { display: flex; align-items: center; }
  .brand {
    width: 250px; height: 100%;
    display: flex; flex-direction: column; align-items: center; justify-content: center; gap: 12px;
  }
  .brand-mark { display: flex; align-items: center; gap: 14px; }
  .brand-dot {
    width: 22px; height: 22px; border-radius: 50%;
    background: var(--white);
  }
  .brand-name {
    font-weight: 900; font-size: 64px; letter-spacing: 2px;
    color: var(--white); line-height: 1;
  }
  .company-name {
    font-size: 11px; letter-spacing: 1px; text-transform: uppercase;
    color: var(--soft);
  }
  .divider {
    width: 1px; height: 210px;
    background: linear-gradient(to bottom, rgba(255,255,255,0), rgba(255,255,255,0.4), rgba(255,255,255,0));
  }
  .details { padding-left: 30px; color: var(--white); }
  .person-title {
    font-size: 12px; letter-spacing: 1px; color: var(--soft);
    margin-bottom: 3px;
  }
  .person-name {
    font-size: 27px; letter-spacing: 1.5px; text-transform: uppercase;
    font-weight: 400; line-height: 1.1;
  }
  .person-name strong { font-weight: 900; }
  .person-role {
    font-size: 12.5px; color: var(--soft); line-height: 1.35;
    margin-top: 6px; margin-bottom: 16px;
  }
  .contact-list { list-style: none; }
  .contact-list li {
    display: flex; align-items: center; gap: 10px;
    font-size: 15px; line-height: 1.65; color: var(--white);
  }
  .contact-list svg { width: 14px; height: 14px; fill: var(--white); flex: none; }
  /* back */
  .card-back { display: flex; align-items: center; justify-content: center; }
  .emboss-name {
    font-weight: 900; font-size: 130px; letter-spacing: 4px;
    color: var(--navy-emboss);
    text-shadow: -1px -1px 0 rgba(255,255,255,0.06), 2px 2px 2px var(--navy-shade);
  }
  .qr-area {
    position: absolute; right: 28px; bottom: 28px;
    width: 76px; height: 76px; border-radius: 3px;
    background: var(--white);
  }
</style>
</head>
<body>
<main class="sheet">
  <section class="card card-front" aria-label="Business card front">
    <div class="brand">
      <div class="brand-mark">
        <span class="brand-dot"></span>
        <span class="brand-name">OKR</span>
      </div>
      <span class="company-name">OKR Handelsagenturen GmbH</span>
    </div>
    <div class="divider"></div>
    <div class="details">
      <p class="person-title">Dipl.-Ing.</p>
      <h1 class="person-name">Lukas <strong>Fenwald</strong></h1>
      <p class="person-role">Managing Director of Operations &amp;<br>Corporate Development</p>
      <ul class="contact-list">
        <li>
          <svg viewBox="0 0 24 24"><path d="M6.6 10.8a15.1 15.1 0 0 0 6.6 6.6l2.2-2.2c.3-.3.7-.4 1-.2 1.1.4 2.3.6 3.6.6.6 0 1 .4 1 1V20c0 .6-.4 1-1 1A17 17 0 0 1 3 4c0-.6.4-1 1-1h3.5c.6 0 1 .4 1 1 0 1.3.2 2.5.6 3.6.1.3 0 .7-.2 1z"/></svg>
          +43 4186 5921 48
        </li>
        <li>
          <svg viewBox="0 0 24 24"><path d="M7 1h10a2 2 0 0 1 2 2v18a2 2 0 0 1-2 2H7a2 2 0 0 1-2-2V3a2 2 0 0 1 2-2zm0 3v14h10V4zm5 15.5a1.2 1.2 0 1 0 0 2.4 1.2 1.2 0 0 0 0-2.4z"/></svg>
          +43 664 58 37 216
        </li>
        <li>
          <svg viewBox="0 0 24 24"><path d="M2 5h20v14H2zm2 2v.4l8 5.3 8-5.3V7zm0 2.8V17h16V9.8l-8 5.3z"/></svg>
          lukas.fenwald@okr-gmbh.at
        </li>
        <li>
          <svg viewBox="0 0 24 24"><path d="M12 2a10 10 0 1 0 0 20 10 10 0 0 0 0-20zm6.9 6h-3a15.6 15.6 0 0 0-1.3-3.9A8 8 0 0 1 18.9 8zM12 4c.8 1.2 1.5 2.5 1.9 4h-3.8c.4-1.5 1.1-2.8 1.9-4zM4.3 14a8 8 0 0 1 0-4h3.4a16.5 16.5 0 0 0 0 4zm.8 2h3a15.6 15.6 0 0 0 1.3 3.9A8 8 0 0 1 5.1 16zm3-8h-3a8 8 0 0 1 4.3-3.9C8.8 5.3 8.4 6.6 8.1 8zM12 20c-.8-1.2-1.5-2.5-1.9-4h3.8c-.4 1.5-1.1 2.8-1.9 4zm2.3-6H9.7a14.7 14.7 0 0 1 0-4h4.6a14.7 14.7 0 0 1 0 4zm.3 5.9c.6-1.2 1-2.5 1.3-3.9h3a8 8 0 0 1-4.3 3.9zm1.7-5.9a16.5 16.5 0 0 0 0-4h3.4a8 8 0 0 1 0 4z"/></svg>
          www.okr-gmbh.at
        </li>
      </ul>
    </div>
  </section>

  <section class="card card-back" aria-label="Business card back">
    <span class="emboss-name">OKR</span>
    <div class="qr-area" role="img" aria-label="QR code with the card's contact details"></div>
  </section>
</main>
</body>
</html>
```